Music Festival Business Cards

The Lantern Gathering
Produced by Bramblewood Sound Collective LLC
New music festival in Arkansas.

Target Market(s)

18-35 year olds

Industry/Entity Type

Festival

Contact Information for Business Card

We are a 5-partner team producing a music festival in Arkansas. We need slick business cards, and I want them to be square.

Requirements
Must have
• I NEED THESE TO BE IN SQUARE SIZE - 2x2 or 2.5x2.5... please not regular size.
• I need www.lanternmeet.example as the link to website.

```html
<!DOCTYPE html>
<html lang="en">
<head>
<meta charset="utf-8">
<title>The Lantern Gathering — Square Business Cards</title>
<link href="https://fonts.googleapis.com/css2?family=Exo+2:wght@600&family=Work+Sans:wght@300;400&display=swap" rel="stylesheet">
<style>
  :root {
    --backdrop: #2a2a2c;
    --card: #1d1e20;
    --card-edge: #303134;
    --silver: #b9bbbe;
    --cyan: #3cc6d6;
    --ink-light: #e6e7e8;
  }
  * { margin: 0; padding: 0; box-sizing: border-box; }
  html, body { width: 1200px; height: 900px; overflow: hidden; }
  body {
    background: var(--backdrop);
    font-family: "Work Sans", sans-serif;
    position: relative;
  }
  .card {
    position: absolute;
    top: 200px;
    width: 500px; height: 500px;
    background: linear-gradient(135deg, #232427 0%, var(--card) 60%, #1a1b1d 100%);
    border: 1px solid var(--card-edge);
    box-shadow: 0 18px 40px rgba(0,0,0,0.45);
  }
  .brand-mark { border: 3px solid var(--silver); }
  .brand-name {
    font-family: "Exo 2", sans-serif; font-weight: 600;
    text-transform: uppercase; text-align: center;
  }

  .card-front {
    left: 70px;
    display: flex; flex-direction: column; align-items: center; justify-content: center; gap: 30px;
  }
  .card-front .brand-mark { width: 40px; height: 40px; }
  .card-front .brand-name { color: var(--silver); font-size: 34px; letter-spacing: 5px; line-height: 1.3; }

  .card-back {
    left: 630px;
    padding: 0 30px;
    display: flex; align-items: center;
  }
  .back-brand {
    width: 180px; flex: none;
    display: flex; flex-direction: column; align-items: center; gap: 18px;
  }
  .back-brand .brand-mark { border-color: var(--cyan); width: 34px; height: 34px; }
  .back-brand .brand-name { color: var(--cyan); font-size: 20px; letter-spacing: 2px; line-height: 1.3; }
  .divider { width: 2px; height: 190px; background: var(--ink-light); flex: none; }
  .contact {
    padding-left: 22px; min-width: 0;
    color: var(--ink-light); font-weight: 300; font-size: 14px; line-height: 1.5;
  }
  .person-name {
    font-family: "Exo 2", sans-serif; font-weight: 600; color: var(--cyan);
    font-size: 22px; letter-spacing: 1.5px; text-transform: uppercase; line-height: 1.1;
  }
  .person-role { font-size: 14px; margin-bottom: 14px; }
  .address { margin-bottom: 8px; }
  .contact-row { display: flex; align-items: center; gap: 9px; white-space: nowrap; }
  .contact-row svg { width: 13px; height: 13px; flex: none; }
</style>
</head>
<body>
  <section class="card card-front">
    <div class="brand-mark"></div>
    <div class="brand-name">The Lantern<br>Gathering</div>
  </section>

  <section class="card card-back">
    <div class="back-brand">
      <div class="brand-mark"></div>
      <div class="brand-name">The Lantern<br>Gathering</div>
    </div>
    <div class="divider"></div>
    <div class="contact">
      <div class="person-name">Rowan Ellery</div>
      <div class="person-role">Director</div>
      <div class="address">418 Birchwood Row<br>Fayetteville, AR 72701</div>
      <div class="contact-row">
        <svg viewBox="0 0 16 16" fill="none" stroke="var(--cyan)" stroke-width="1.6" stroke-linecap="round"><path d="M4 2l2.5 3-1.5 1.5c.8 1.8 2.2 3.2 4 4L10.5 9l3 2.5-1.5 2C7 13 3 9 2.5 4z"/></svg>
        <span>479 555 0182</span>
      </div>
      <div class="contact-row">
        <svg viewBox="0 0 16 16" fill="none" stroke="var(--cyan)" stroke-width="1.6"><rect x="2" y="4" width="12" height="8.5"/><path d="M2 4l6 5 6-5"/></svg>
        <span>hello@lanternmeet.example</span>
      </div>
      <div class="contact-row">
        <svg viewBox="0 0 16 16" fill="none" stroke="var(--cyan)" stroke-width="1.4"><circle cx="8" cy="8" r="6"/><ellipse cx="8" cy="8" rx="2.6" ry="6"/><path d="M2 8h12"/></svg>
        <span>www.lanternmeet.example</span>
      </div>
    </div>
  </section>
</body>
</html>
```